Business Intelligence Application - Reporting Menu and Report Criteria Design

Looking for a fresh, effective and user friendly view for the menu structure and reporting criteria screen format for a business reporting application. Initial format completed, content structure is in place, but we need the 'wow' design.. as its a serious professional report/BI tool it has to fall within certain guidelines for clarity and graphics..but we want it to be slick, friendly, great user experience. There is a large amount of complex content to fit into a small space and we need it to be very inviting, modern and intuitive.. If interested, please review the attachment. We have live screens in operation, but feel these could be improved and looking forward to seeing what great creative suggestions could be made. Please review work done to date in the attached.. We are not looking for a total re-design of everything, all the basic business content/structure is there.. but tell us what we could do to improve this in terms of graphic design... particularly the criteria screens.. thanks!
Updates

Reason: Need a few more days to review designs - thanks for all submissions so far, we will make a selection shortly.

Target Market(s)

Business analysts, hotel operations teams, finance analysts hospitality industry

Industry/Entity Type

Hospitality

Coding

Coded - Design and coding required

Number of Pages Required

4 page

Font styles to use
Sans Serif
Other font styles liked:
• Candara, please see example in deck

Colors
3276b5
3176b5
0255a3
85acd3
33a6d7
cee9f5
85cae6

Requirements
Must have
• sharp clear, logical menu structure, (currently it has 'clicks to sub-menus, we need hover over, slide to sub-menus..) colour, styling.. and most focus on revision of criteria.. right now is somewhat heavy, cumbersome.. keep colour and friendly intuitive process steps.. its heavy analytical stuff.. best of luck!
Should not have
• No grey fonts on white or grey screens! many business apps are not readable or sharp.. or fonts are too small.. colourless, so please avoid that.. see our deck - sharp dark (navy) or black fonts on white, or light shading..

```html
<!DOCTYPE html>
<html lang="en">
<head>
<meta charset="utf-8">
<title>Yieldline – Select Property</title>
<link rel="stylesheet" href="https://fonts.googleapis.com/css2?family=Raleway:ital,wght@0,400;0,500;0,600;0,700;1,500&family=Open+Sans:wght@400;600;700&display=swap">
<style>
  :root {
    --navy: #021738;
    --sky: #33a6d7;
    --sky-pale: #cee9f5;
    --blue-deep: #0255a3;
    --ink: #2b2b2b;
    --ink-soft: #3c3c3c;
    --row-alt: #f4f4f4;
    --border: #d4d4d4;
    --scroll: #dcdcdc;
    --white: #ffffff;
  }
  * { box-sizing: border-box; margin: 0; padding: 0; }
  html, body { width: 1200px; height: 738px; overflow: hidden; background: var(--white); }
  body { position: relative; font-family: "Raleway", sans-serif; color: var(--ink); }

  .brand-bar { position: absolute; left: 0; top: 0; width: 300px; height: 89px; background: var(--navy); display: flex; align-items: center; padding-left: 61px; }
  .brand-name { font-family: "Raleway", sans-serif; font-weight: 700; font-size: 22px; color: var(--white); }

  .sidebar { position: absolute; left: 0; top: 89px; width: 300px; height: 649px; background: var(--sky); }
  .nav-item { position: absolute; left: 0; width: 300px; height: 30px; display: flex; align-items: center; color: var(--white); font-size: 12px; font-weight: 700; letter-spacing: .3px; }
  .nav-item svg.nav-icon { position: absolute; left: 60px; width: 12px; height: 12px; fill: var(--white); }
  .nav-item .nav-label { position: absolute; left: 94px; }
  .nav-item svg.chev { position: absolute; left: 258px; width: 9px; height: 9px; fill: none; stroke: var(--white); stroke-width: 1.6; }
  .copyright { position: absolute; left: 76px; top: 580px; color: var(--white); font-size: 12.5px; line-height: 21px; }

  .topbar { position: absolute; left: 300px; top: 0; width: 900px; height: 89px; background: var(--sky-pale); }
  .global-search { position: absolute; left: 32px; top: 20px; width: 514px; height: 47px; background: var(--white); border-radius: 2px; }
  .search-avatar { position: absolute; right: 9px; top: 8px; width: 31px; height: 31px; border-radius: 50%; background: radial-gradient(circle at 50% 55%, #c58a55 0 40%, #7a4420 60%); border: 2px solid #f0e2d0; }
  .user-badge { position: absolute; left: 571px; top: 20px; width: 49px; height: 49px; border-radius: 50%; border: 2px solid var(--navy); display: flex; align-items: center; justify-content: center; }
  .user-badge svg { width: 22px; height: 22px; fill: var(--blue-deep); }
  .welcome { position: absolute; left: 634px; top: 26px; }
  .welcome-title { font-size: 12.5px; font-weight: 700; color: var(--blue-deep); }
  .welcome-date { font-size: 12px; font-style: italic; font-weight: 500; color: var(--navy); margin-top: 5px; }
  .top-icon { position: absolute; top: 37px; width: 14px; height: 14px; fill: var(--blue-deep); }

  .filter { position: absolute; top: 116px; width: 126px; height: 43px; border: 2px solid var(--border); background: var(--white); font-size: 12.5px; color: var(--ink-soft); display: flex; align-items: center; padding-left: 12px; }
  .filter svg { position: absolute; right: 12px; width: 8px; height: 8px; fill: none; stroke: var(--ink-soft); stroke-width: 1.5; }

  .property-panel { position: absolute; left: 330px; top: 202px; width: 810px; height: 248px; border: 1px solid var(--border); border-radius: 3px; overflow: hidden; }
  .panel-head { height: 44px; background: var(--sky); display: flex; align-items: center; padding-left: 17px; color: var(--white); font-family: "Open Sans", sans-serif; font-weight: 700; font-size: 17px; position: relative; }
  .panel-head svg { position: absolute; top: 15px; width: 15px; height: 15px; fill: none; stroke: var(--white); stroke-width: 2.4; stroke-linecap: round; }
  .rows { position: relative; height: 203px; }
  .row { height: 49px; display: flex; align-items: center; justify-content: space-between; padding: 0 42px 0 17px; font-family: "Open Sans", sans-serif; font-size: 15px; color: var(--ink); }
  .row:nth-child(odd) { background: var(--white); color: var(--blue-deep); font-weight: 600; }
  .row:nth-child(even) { background: var(--row-alt); }
  .row .code { color: var(--ink); font-weight: 400; min-width: 52px; text-align: right; }
  .row:nth-child(even) .code { padding-right: 27px; }
  .scrollbar { position: absolute; right: 0; top: 0; width: 25px; height: 100%; background: var(--scroll); }
  .scrollbar svg { position: absolute; left: 8px; width: 9px; height: 6px; fill: #333; }
</style>
</head>
<body>
  <header class="brand-bar"><span class="brand-name">Yieldline</span></header>

  <nav class="sidebar">
    <div class="nav-item" style="top:36px">
      <svg class="nav-icon" viewBox="0 0 12 12"><circle cx="6" cy="3.5" r="3"/><path d="M1 12c0-3.5 2-5.5 5-5.5s5 2 5 5.5z"/></svg>
      <span class="nav-label">ADMIN</span>
      <svg class="chev" viewBox="0 0 9 9"><path d="M1.5 3l3 3 3-3"/></svg>
    </div>
    <div class="nav-item" style="top:85px">
      <svg class="nav-icon" viewBox="0 0 12 12" style="width:14px;left:59px"><circle cx="6" cy="3.5" r="2.3"/><circle cx="2.3" cy="4.5" r="1.7"/><circle cx="9.7" cy="4.5" r="1.7"/><path d="M2.5 11c0-3 1.5-4.5 3.5-4.5s3.5 1.5 3.5 4.5zM0 10c0-2 .9-3.2 2.3-3.2.7 0 1 .2 1 .2-.6.8-1 1.8-1 3zM12 10c0-2-.9-3.2-2.3-3.2-.7 0-1 .2-1 .2.6.8 1 1.8 1 3z"/></svg>
      <span class="nav-label">MANAGEMENT</span>
      <svg class="chev" viewBox="0 0 9 9"><path d="M3 1.5l3 3-3 3"/></svg>
    </div>
    <div class="nav-item" style="top:134px">
      <svg class="nav-icon" viewBox="0 0 12 12"><path d="M5 0a5 5 0 1 0 2.7 9.2L10.5 12 12 10.5 9.2 7.7A5 5 0 0 0 5 0zm0 2a3 3 0 1 1 0 6 3 3 0 0 1 0-6z"/></svg>
      <span class="nav-label">PROPERTY SEARCH</span>
      <svg class="chev" viewBox="0 0 9 9"><path d="M3 1.5l3 3-3 3"/></svg>
    </div>
    <div class="nav-item" style="top:183px">
      <svg class="nav-icon" viewBox="0 0 12 12"><path d="M5 0h2l.3 1.6 1.3.6 1.4-.9 1.4 1.4-.9 1.4.6 1.3L12 5v2l-1.6.3-.6 1.3.9 1.4-1.4 1.4-1.4-.9-1.3.6L7 12H5l-.3-1.6-1.3-.6-1.4.9-1.4-1.4.9-1.4-.6-1.3L0 7V5l1.6-.3.6-1.3-.9-1.4 1.4-1.4 1.4.9 1.3-.6zM6 4a2 2 0 1 0 0 4 2 2 0 0 0 0-4z"/></svg>
      <span class="nav-label">INTEL</span>
      <svg class="chev" viewBox="0 0 9 9"><path d="M3 1.5l3 3-3 3"/></svg>
    </div>
    <div class="nav-item" style="top:232px">
      <svg class="nav-icon" viewBox="0 0 12 12"><path d="M2 0h5.5L10 2.5V12H2zM3.5 6h5v1h-5zm0 2h5v1h-5zM7 0v3h3z"/></svg>
      <span class="nav-label">PLANNING</span>
      <svg class="chev" viewBox="0 0 9 9"><path d="M3 1.5l3 3-3 3"/></svg>
    </div>
    <p class="copyright">Copyright © 2017. Company Name<br>All Right Reserved</p>
  </nav>

  <section class="topbar">
    <div class="global-search"><span class="search-avatar" role="img" aria-label="User avatar"></span></div>
    <div class="user-badge"><svg viewBox="0 0 22 22"><circle cx="11" cy="6.5" r="5"/><path d="M2 21c0-6 4-8.5 9-8.5s9 2.5 9 8.5z"/></svg></div>
    <div class="welcome">
      <div class="welcome-title">WELCOME ADMIN</div>
      <div class="welcome-date">Tuesday Oct 3, 2017</div>
    </div>
    <svg class="top-icon" style="left:790px" viewBox="0 0 14 14"><path d="M7 0a1 1 0 0 1 1 1v.6A4.5 4.5 0 0 1 11.5 6v3.5L13 11H1l1.5-1.5V6A4.5 4.5 0 0 1 6 1.6V1a1 1 0 0 1 1-1zM5.3 12h3.4a1.7 1.7 0 0 1-3.4 0z"/></svg>
    <svg class="top-icon" style="left:825px" viewBox="0 0 14 14"><path d="M1 2h5v2H3v6h3v2H1zM7 4.5h3V2l4 5-4 5V9.5H7z"/></svg>
  </section>

  <div class="filter" style="left:332px">Search Name</div>
  <div class="filter" style="left:469px">Search ID</div>
  <div class="filter" style="left:605px">Search Product</div>
  <div class="filter" style="left:742px">Divisions<svg viewBox="0 0 8 8"><path d="M1 2.5l3 3 3-3"/></svg></div>
  <div class="filter" style="left:877px">Regions<svg viewBox="0 0 8 8"><path d="M1 2.5l3 3 3-3"/></svg></div>
  <div class="filter" style="left:1013px">Areas<svg viewBox="0 0 8 8"><path d="M1 2.5l3 3 3-3"/></svg></div>

  <section class="property-panel">
    <div class="panel-head">Select Property
      <svg style="left:732px" viewBox="0 0 15 15"><path d="M12.5 6A5.3 5.3 0 0 0 2.6 4.8M2.5 9a5.3 5.3 0 0 0 9.9 1.2"/><path d="M2.4 1.5v3.5h3.5M12.6 13.5V10H9.1" stroke-linecap="butt"/></svg>
      <svg style="left:777px;width:13px;height:13px;top:16px" viewBox="0 0 13 13"><path d="M2 2l9 9M11 2l-9 9"/></svg>
    </div>
    <div class="rows">
      <div class="row"><span>Harbor Crest Hotel &amp; Towers</span><span class="code">RHDOH</span></div>
      <div class="row"><span>Coral Bay Hotel</span><span class="code">123</span></div>
      <div class="row"><span>Harbor Crest Hotel &amp; Towers</span><span class="code">RHDOH</span></div>
      <div class="row"><span>Coral Bay Hotel</span><span class="code">123</span></div>
      <div class="scrollbar">
        <svg style="top:8px" viewBox="0 0 9 6"><path d="M4.5 0L9 6H0z"/></svg>
        <svg style="bottom:8px" viewBox="0 0 9 6"><path d="M0 0h9L4.5 6z"/></svg>
      </div>
    </div>
  </section>
</body>
</html>
```